Design an Elegant Handbag Brand website

I need a webiste design are looking for ideas for a new theme, color scheme, etc. You come up with the general look and feel of the home page and our team will take it from there.
We're only looking for a one (1) page layout which should be fashionable and graphic intensive, but also include the standard homepage links (about us, see our collections, etc)

Target Market(s)

Our customers are fashionable women looking for an animal friendly and environmentally friendly handbag.

Industry/Entity Type

Business

Number of Pages Required

1 page

Font styles to use
Serif
Sans Serif

Requirements
Must have
• Feel free to modify it with different colors or tweaks as you see fit. We are open to all suggestions.
Nice to have

```html
<!DOCTYPE html>
<html lang="en">
<head>
<meta charset="utf-8">
<title>Aurelle — Summer New Collection</title>
<link href="https://fonts.googleapis.com/css2?family=Bodoni+Moda:wght@500&family=Lato:wght@300&family=Open+Sans:wght@400;600;700&display=swap" rel="stylesheet">
<style>
  :root {
    --page-bg: #e7e7e7;
    --card-bg: #ffffff;
    --brown: #8c5f3f;
    --ink: #333333;
    --white: #ffffff;
    --field: #f3ede8;
  }
  * { margin: 0; padding: 0; box-sizing: border-box; }
  html, body { width: 1200px; height: 900px; overflow: hidden; background: var(--page-bg); }
  .canvas { position: relative; width: 1200px; height: 900px; }
  .site-card {
    position: absolute; left: 49px; top: 140px; width: 1105px; height: 620px;
    background: var(--card-bg); border-radius: 14px; overflow: hidden;
    box-shadow: 0 3px 6px rgba(0,0,0,0.22);
  }
  .brand-rail { position: absolute; left: 0; top: 0; width: 93px; height: 100%; }
  .brand-name {
    position: absolute; left: 46px; top: 444px;
    transform: translate(-50%, -50%) rotate(-90deg);
    font-family: "Open Sans", sans-serif; font-weight: 600; font-size: 31px;
    letter-spacing: 6px; color: var(--ink); white-space: nowrap;
  }
  .brand-dot {
    position: absolute; left: 59px; top: 229px; width: 6px; height: 6px;
    border: 1px solid var(--ink); border-radius: 50%;
  }
  .hero {
    position: absolute; left: 93px; top: 0; width: 805px; height: 100%;
  }
  .hero-photo {
    position: absolute; inset: 0;
    background:
      radial-gradient(ellipse 220px 250px at 470px 360px, #eadbc8 0%, #e6d3bd 60%, rgba(230,211,189,0) 100%),
      linear-gradient(90deg, #b9b3b1 0%, #d9cfca 22%, #c99ac9 32%, #c98ccc 60%, #c27fc6 100%);
  }
  .hero-title {
    position: absolute; left: 19px; top: 58px;
    font-family: "Bodoni Moda", serif; font-weight: 500; font-size: 96px;
    letter-spacing: 9px; color: var(--white); line-height: 1;
  }
  .hero-subtitle {
    position: absolute; left: 19px; top: 146px;
    font-family: "Lato", sans-serif; font-weight: 300; font-size: 52px;
    letter-spacing: 7px; color: var(--white); line-height: 1;
  }
  .hero-cta {
    position: absolute; left: 145px; top: 219px; width: 87px; height: 26px;
    border: 1.5px solid var(--white); color: var(--white);
    font-family: "Open Sans", sans-serif; font-size: 13px;
    display: flex; align-items: center; justify-content: center; text-decoration: none;
  }
  .main-nav { position: absolute; left: 935px; top: 0; width: 170px; height: 100%; }
  .nav-link {
    position: absolute; left: 0;
    font-family: "Open Sans", sans-serif; font-size: 15px; line-height: 14px;
    color: var(--brown); text-decoration: none; letter-spacing: 0.3px;
  }
  .nav-link.is-active::after {
    content: ""; position: absolute; left: 111px; top: 7px; width: 60px; height: 2px;
    background: var(--brown);
  }
  .cart-icon { position: absolute; left: 0; top: 232px; }
  .search-field {
    position: absolute; left: 0; top: 582px; width: 150px; height: 13px;
    background: var(--field); border-bottom: 1px solid var(--brown);
    font-family: "Open Sans", sans-serif; font-size: 9px; font-style: italic;
    color: var(--brown); padding-left: 1px; line-height: 12px;
  }
  .search-field svg { position: absolute; right: 2px; top: 2px; }
</style>
</head>
<body>
<div class="canvas">
  <div class="site-card">
    <aside class="brand-rail">
      <span class="brand-dot"></span>
      <div class="brand-name">AURELLE</div>
    </aside>

    <section class="hero">
      <div class="hero-photo" role="img" aria-label="Cream quilted leather handbag with gold handle held by a woman in a pink dress against a painted wall"></div>
      <h1 class="hero-title">SUMMER</h1>
      <p class="hero-subtitle">New collection</p>
      <a class="hero-cta" href="#">Explore</a>
    </section>

    <nav class="main-nav">
      <a class="nav-link is-active" href="#" style="top:36px">HOME</a>
      <a class="nav-link" href="#" style="top:80px">NEW<br>COLLECTION</a>
      <a class="nav-link" href="#" style="top:138px">SHOP</a>
      <a class="nav-link" href="#" style="top:191px">ABOUT US</a>
      <svg class="cart-icon" width="26" height="28" viewBox="0 0 26 28" aria-label="Cart">
        <path d="M2 9 H19 L20 26 H1 Z" fill="none" stroke="#8c5f3f" stroke-width="1.3"/>
        <path d="M6 11 V6 a4.5 4.5 0 0 1 9 0 V11" fill="none" stroke="#8c5f3f" stroke-width="1.3"/>
        <circle cx="20.5" cy="5" r="4" fill="#8c5f3f"/>
        <text x="20.5" y="7.2" font-size="6" font-family="Open Sans, sans-serif" fill="#fff" text-anchor="middle">1</text>
      </svg>
      <div class="search-field">Search
        <svg width="8" height="8" viewBox="0 0 8 8"><circle cx="3.2" cy="3.2" r="2.3" fill="none" stroke="#8c5f3f" stroke-width="0.9"/><line x1="5" y1="5" x2="7.5" y2="7.5" stroke="#8c5f3f" stroke-width="0.9"/></svg>
      </div>
    </nav>
  </div>
</div>
</body>
</html>
```